Alder Coach and Spa Service Van Wrap Design

Alder Coach Repair and Spa Vehicle Wrap Design

Project goal: To design a vehicle wrap for a service van that aligns with existing branding and logos of Alder Coach Repair and Spa.
Scope of work: - Design a vehicle wrap that incorporates Alder Coach Repair and Spa’s branding and logos. - Ensure the design highlights services such as Maintenance & Repair, Oil Change & Lube, Slide Outs & Awnings, Tires & Brakes, RV Spa & Detailing, Leveling Systems, AC & Heating. - Create a visually appealing and informative wrap that effectively communicates the services and professionalism of certified techs. Company phone number (888) 514-2086 and website www.aldercoachfix.com

Fonts: Gotham HTF medium and Gotham HTF Book
Pantones: 320 C and Cool Gray 9 C
#009ca6 and #75787b

Target Market(s)

RV Owners

Industry/Entity Type

RV Repair and RV Spa

• Gotham HTF

Colors
00AB8E
00BBA5
67D7C9
C6EFE9
E9F9F6

Requirements
Must have
• Our fonts, logo, brand colors, list of services, contact information. Morlund Trekker Long Van is the vehicle.
Nice to have
• Eye-catching design, with an emphasis on "RV Repair & Spa" to generate interest in our services (make that the largest part of the design.
Should not have
• Do not include the person in the design.

```html
<!DOCTYPE html>
<html lang="en">
<head>
<meta charset="utf-8">
<title>Alder Coach Repair and Spa — Service Van Wrap</title>
<link rel="stylesheet" href="https://fonts.googleapis.com/css2?family=Montserrat:wght@400;500;600&family=Oswald:wght@400;500&family=Roboto+Condensed:wght@700&display=swap">
<style>
  :root {
    --brand-teal: #009ca6;
    --brand-gray: #75787b;
    --wrap-white: #f4f5f5;
    --band-gray: #7d8083;
    --glass: #8f9497;
    --trim-dark: #2b2d2f;
    --tire: #1c1d1e;
    --hub: #c9cccd;
    --silver: #b9bcbe;
    --page: #ffffff;
  }
  html, body {
    margin: 0;
    width: 1200px;
    height: 1200px;
    overflow: hidden;
    background: var(--page);
  }
  .wrap-sheet { display: block; width: 1200px; height: 1200px; }
  .brand-name { font-family: "Montserrat", sans-serif; font-weight: 600; fill: var(--brand-teal); }
  .brand-tagline { font-family: "Montserrat", sans-serif; font-weight: 400; fill: var(--brand-gray); }
  .service-list { font-family: "Oswald", sans-serif; font-weight: 400; font-size: 9px; fill: #ffffff; letter-spacing: 0.2px; }
  .service-dot { fill: var(--brand-teal); }
  .web-address { font-family: "Montserrat", sans-serif; font-weight: 500; font-size: 10px; }
  .phone-number { font-family: "Roboto Condensed", sans-serif; font-weight: 700; font-size: 23px; fill: #ffffff; letter-spacing: 0.5px; }
  .body-white { fill: var(--wrap-white); }
  .body-teal { fill: var(--brand-teal); }
  .body-band { fill: var(--band-gray); }
  .band-rule { stroke: #ffffff; stroke-width: 1.2; }
  .panel-seam { stroke: #6c7072; stroke-width: 0.8; fill: none; opacity: 0.55; }
  .cab-glass { fill: var(--glass); }
  .trim { fill: var(--trim-dark); }
  .tire { fill: var(--tire); }
  .hub { fill: var(--hub); }
  .silver-stripe { fill: var(--silver); }
  .brand-dot { fill: var(--brand-teal); }
  .icon-slot { fill: #a5a8aa; }
</style>
</head>
<body>
<svg class="wrap-sheet" viewBox="0 0 1200 1200" xmlns="http://www.w3.org/2000/svg">
  <defs>
    <path id="van-body" d="M40 2 L640 8 Q660 10 672 24 L722 90 L805 118 Q822 126 825 150 L828 205 Q828 220 815 220 L12 220 Q4 220 4 208 L8 60 Q12 6 40 2 Z"/>
    <clipPath id="van-clip"><use href="#van-body"/></clipPath>

    <g id="load-area-art">
      <circle class="brand-dot" cx="120" cy="60" r="46"/>
      <text class="brand-name" x="200" y="62" font-size="40" textLength="280" lengthAdjust="spacingAndGlyphs">ALDER COACH</text>
      <text class="brand-tagline" x="200" y="100" font-size="28" textLength="280" lengthAdjust="spacingAndGlyphs">REPAIR &amp; SPA</text>

      <rect class="icon-slot" x="36" y="121" width="58" height="28" rx="3" role="img" aria-label="Small motorhome icon"/>
      <rect class="icon-slot" x="462" y="122" width="28" height="26" rx="13" role="img" aria-label="Wrench and gear service icon"/>

      <text class="service-list" x="108" y="131">MAINTENANCE &amp; REPAIR <tspan class="service-dot">•</tspan> OIL CHANGE &amp; LUBE <tspan class="service-dot">•</tspan> SLIDE OUTS &amp; AWNINGS <tspan class="service-dot">•</tspan> TIRES &amp; BRAKES</text>
      <text class="service-list" x="170" y="145">RV SPA &amp; DETAILING <tspan class="service-dot">•</tspan> LEVELING SYSTEMS <tspan class="service-dot">•</tspan> AC &amp; HEATING</text>
    </g>

    <g id="van-hardware">
      <path class="cab-glass" d="M528 18 L632 18 Q648 20 660 34 L700 88 L528 88 Z"/>
      <path class="panel-seam" d="M300 12 L300 212 M392 12 L392 212 M500 12 L500 212 M525 12 L525 212"/>
      <rect class="trim" x="0" y="185" width="22" height="16" rx="3"/>
      <rect class="trim" x="812" y="170" width="20" height="30" rx="4"/>
      <rect x="4" y="40" width="8" height="48" rx="2" fill="#b32b2b"/>
      <rect x="812" y="128" width="14" height="28" rx="3" fill="#e08a2e"/>
    </g>

    <g id="van-wheels">
      <circle class="tire" cx="155" cy="222" r="50"/>
      <circle class="hub" cx="155" cy="222" r="27"/>
      <circle class="tire" cx="695" cy="222" r="50"/>
      <circle class="hub" cx="695" cy="222" r="27"/>
    </g>
  </defs>

  <!-- Variant A: white cab -->
  <g class="van van-white-cab" transform="translate(75 275) scale(1.25)">
    <g clip-path="url(#van-clip)">
      <rect class="body-white" x="0" y="0" width="840" height="115"/>
      <rect class="body-band" x="0" y="115" width="840" height="40"/>
      <line class="band-rule" x1="0" y1="117" x2="840" y2="117"/>
      <line class="band-rule" x1="0" y1="153" x2="840" y2="153"/>
      <rect class="body-teal" x="0" y="155" width="840" height="70"/>
      <use href="#van-hardware"/>
      <use href="#load-area-art"/>
      <text class="web-address" x="530" y="110" fill="var(--brand-teal)">www.aldercoachfix.com</text>
      <text class="phone-number" x="527" y="146">(888) 514-2086</text>
    </g>
    <use href="#van-wheels"/>
  </g>

  <!-- Variant B: teal cab with silver sweep -->
  <g class="van van-teal-cab" transform="translate(75 725) scale(1.25)">
    <g clip-path="url(#van-clip)">
      <rect class="body-white" x="0" y="0" width="840" height="115"/>
      <rect class="body-band" x="0" y="115" width="840" height="40"/>
      <line class="band-rule" x1="0" y1="117" x2="840" y2="117"/>
      <line class="band-rule" x1="0" y1="153" x2="840" y2="153"/>
      <rect class="body-teal" x="0" y="155" width="840" height="70"/>
      <path class="body-teal" d="M520 0 L840 0 L840 225 L526 225 Q546 120 520 0 Z"/>
      <path class="silver-stripe" d="M496 0 L520 0 Q546 120 526 225 L502 225 Q522 120 496 0 Z"/>
      <use href="#van-hardware"/>
      <use href="#load-area-art"/>
      <text class="web-address" x="564" y="112" fill="#ffffff">www.aldercoachfix.com</text>
      <text class="phone-number" x="561" y="146">(888) 514-2086</text>
    </g>
    <use href="#van-wheels"/>
  </g>
</svg>
</body>
</html>
```